Personal Vistrano Banner

I am creating a personal brand for myself. I want a vistrano banner that inspires and motivates people to reach their epic awesomeness. I am creating and designing my personal brand. It can be a background with words on a scenery a picture or 3d graphic. If someone looked at it, they should say it is aggressively epic and motivating. It should be dramatic and bold.
My personal goal is to help as many people reach financial freedom as possible, and challenge and break their own limiting beliefs. This personal brand will be integrated into my zomblat, quorVex, and professional vistrano fanpage (in addition to personal page). My goals are to open up a school for the underpriveleged children, develop my network marketing company team, and become a billionaire in the process. I want to attract people to me that really identify with doing what most think is impossible in terms of personal growth, impact to the world and financial wealth.
Updates

I have updated my brief with more background, and added a new comment to the discussion section to give you more to work with.

Reason: To give designers more time and to create a second and third place prize.

Reason: I am giving designers time to submit more designs

Target Market(s)

business professionals, and people with an entrepreneurial spirit.

Industry/Entity Type

Financial

Requirements
Must have
• It must be the exact dimensions required for vistrano banners. It should not be bigger or smaller. exact!!!

```html
<!DOCTYPE html>
<html lang="en">
<head>
<meta charset="utf-8">
<title>Reach Your Epic Awesomeness — Vistrano Banner</title>
<link href="https://fonts.googleapis.com/css2?family=Russo+One&display=swap" rel="stylesheet">
<style>
  :root {
    --sky-deep: #1d1850;
    --sky-mid: #3b2f86;
    --sky-light: #7a6fc4;
    --storm-glow: #c9c3f0;
    --band-dark: #3a3a3c;
    --band-mid: #545456;
    --floor-light: #9a9a9c;
    --floor-dark: #5a5a5c;
    --reach-face: #232325;
    --reach-side: #121213;
    --epic-face: #c21a17;
    --epic-side: #6d0b0a;
    --awe-face: #c4c4c6;
    --awe-top: #ececee;
    --awe-side: #6e6e70;
  }
  * { margin: 0; padding: 0; box-sizing: border-box; }
  html, body { width: 1200px; height: 444px; overflow: hidden; background: #000; }
  .banner {
    position: relative;
    width: 1200px;
    height: 444px;
    overflow: hidden;
    font-family: "Russo One", sans-serif;
    text-transform: uppercase;
  }
  .storm-sky {
    position: absolute; inset: 0;
    width: 1200px; height: 444px;
  }
  .stage {
    position: absolute; inset: 0;
    width: 1200px; height: 444px;
  }
  .headline { position: absolute; white-space: nowrap; line-height: 1; }
  .reach {
    left: 34px; top: 110px;
    font-size: 72px;
    letter-spacing: 4px;
    color: var(--reach-face);
    transform-origin: left top;
    transform: scale(1.02, 1.1);
    text-shadow:
      1px 1px 0 var(--reach-side), 2px 2px 0 var(--reach-side),
      3px 3px 0 var(--reach-side), 4px 4px 0 var(--reach-side),
      5px 5px 0 var(--reach-side);
  }
  .epic {
    left: 548px; top: 48px;
    font-size: 150px;
    letter-spacing: 6px;
    color: var(--epic-face);
    transform-origin: left top;
    transform: scale(1.04, 0.98);
    text-shadow:
      -1px 1px 0 var(--epic-side), -2px 2px 0 var(--epic-side),
      -3px 3px 0 var(--epic-side), -4px 4px 0 var(--epic-side),
      -5px 5px 0 var(--epic-side), -6px 6px 0 var(--epic-side),
      -7px 7px 0 var(--epic-side), -8px 8px 0 var(--epic-side),
      -9px 9px 0 var(--epic-side), -10px 10px 0 var(--epic-side);
  }
  .awesomeness {
    left: 28px; top: 192px;
    font-size: 104px;
    letter-spacing: 2px;
    color: var(--awe-face);
    transform-origin: left top;
    transform: scale(1.33, 1);
    text-shadow:
      0 -2px 0 var(--awe-top),
      1px 2px 0 var(--awe-side), 2px 4px 0 var(--awe-side),
      3px 6px 0 var(--awe-side), 4px 8px 0 var(--awe-side),
      5px 10px 0 var(--awe-side), 6px 12px 0 var(--awe-side),
      7px 14px 0 var(--awe-side), 8px 16px 0 var(--awe-side);
  }
</style>
</head>
<body>
<main class="banner">
  <svg class="storm-sky" viewBox="0 0 1200 444" role="img" aria-label="Stormy violet night sky with lightning bolts and rolling clouds">
    <defs>
      <linearGradient id="skyGradient" x1="0" y1="0" x2="1" y2="0.6">
        <stop offset="0" stop-color="var(--sky-deep)"/>
        <stop offset="0.45" stop-color="var(--sky-mid)"/>
        <stop offset="1" stop-color="var(--sky-light)"/>
      </linearGradient>
      <radialGradient id="stormGlow" cx="0.85" cy="0.25" r="0.4">
        <stop offset="0" stop-color="var(--storm-glow)" stop-opacity="0.55"/>
        <stop offset="1" stop-color="var(--storm-glow)" stop-opacity="0"/>
      </radialGradient>
    </defs>
    <rect width="1200" height="444" fill="url(#skyGradient)"/>
    <rect width="1200" height="444" fill="url(#stormGlow)"/>
  </svg>

  <svg class="stage" viewBox="0 0 1200 444" aria-hidden="true">
    <defs>
      <linearGradient id="floorGradient" x1="0" y1="0" x2="0" y2="1">
        <stop offset="0" stop-color="var(--floor-light)"/>
        <stop offset="1" stop-color="var(--floor-dark)"/>
      </linearGradient>
      <linearGradient id="bandGradient" x1="0" y1="0" x2="0" y2="1">
        <stop offset="0" stop-color="var(--band-mid)"/>
        <stop offset="1" stop-color="var(--band-dark)"/>
      </linearGradient>
    </defs>
    <rect class="title-band" x="0" y="104" width="555" height="90" fill="url(#bandGradient)"/>
    <rect class="lower-band" x="0" y="194" width="1200" height="250" fill="url(#floorGradient)"/>
    <polygon class="ground-slab" points="0,300 1200,330 1200,444 0,444" fill="var(--floor-dark)" opacity="0.6"/>
  </svg>

  <h1 class="headline reach">Reach Your</h1>
  <p class="headline epic">Epic</p>
  <p class="headline awesomeness">Awesomeness</p>
</main>
</body>
</html>
```